Bref créative
RON TALIVERO STATIONARY PACKAGE
Letterhead paper, Envelopes, Business Cards, Patient brochures, Flyer,Gift Certificate, T-Shirts
Professional
RON TALIVERO DDS
General & Cosmetic Dentistry
47-30 91 Street
Elmhurst, NY 11208
brightcuspdental@mailbox-example.com
www.brightcuspdental-example.com
I would like to present a very professional image for my company.
Smile!

```html
<!DOCTYPE html>
<html lang="en">
<head>
<meta charset="utf-8">
<title>Bright Cusp Dental – Stationery</title>
<link rel="stylesheet" href="https://fonts.googleapis.com/css2?family=Open+Sans:wght@400;600&family=Pinyon+Script&display=swap">
<style>
:root{
  --bg:#e4e2de;
  --paper:#ffffff;
  --dark:#1e1f1c;
  --gold:#b3a300;
  --gold-light:#d4c51a;
  --green:#78b41e;
  --green-light:#9bcc3a;
  --ink:#555;
  --ink-soft:#8a8a8a;
}
*{margin:0;padding:0;box-sizing:border-box}
html,body{width:1200px;height:730px;overflow:hidden;background:var(--bg);font-family:"Open Sans",sans-serif;color:var(--ink)}
.canvas{position:relative;width:1200px;height:730px}

.brand{font-family:"Open Sans",sans-serif;font-weight:600;color:var(--gold);display:flex;align-items:center;gap:5px;white-space:nowrap}
.brand-dot{width:8px;height:8px;border-radius:50%;background:var(--green)}

/* cards */
.card{position:absolute;width:150px;height:86px;box-shadow:0 2px 5px rgba(0,0,0,.25);overflow:hidden}
.card--light{background:var(--paper)}
.card--dark{background:var(--dark)}
.card--logo{display:flex;flex-direction:column;align-items:center;justify-content:center}
.card--logo .brand{font-size:11px}
.card-web{position:absolute;bottom:7px;width:100%;text-align:center;font-size:5.5px;color:var(--green)}
.card-stripe{position:absolute;left:0;right:0;bottom:0;height:3px;background:var(--green)}
.card--contact{padding:10px 11px}
.card--contact .brand{font-size:8px;margin-bottom:8px}
.card-name{font-size:7px;font-weight:600;color:var(--green)}
.card-role{font-size:5px;color:var(--ink-soft);margin-bottom:6px}
.card-line{font-size:4.8px;line-height:1.45}
.card--dark .card-line{color:#d8d8d8}
.card--light .card-line{color:var(--ink)}

/* envelopes */
.envelopes{position:absolute;left:120px;top:250px;width:480px;height:450px}
.env-address{position:absolute;left:22px;top:385px;font-size:6.5px;line-height:1.5;color:var(--ink)}
.env-address .card-name{font-size:7px}
.env-brand{position:absolute;left:0;right:0;top:300px;display:flex;justify-content:center}
.env-brand .brand{font-size:14px}
.env-tab{position:absolute;top:0;left:0;right:0;display:flex;justify-content:center;font-size:8px;font-weight:600;color:#fff}

/* letterhead */
.letterhead{position:absolute;left:660px;top:30px;width:470px;height:670px;background:var(--paper);box-shadow:0 3px 8px rgba(0,0,0,.25)}
.lh-brand{position:absolute;left:40px;top:38px}
.lh-brand .brand{font-size:15px}
.lh-address{position:absolute;right:36px;top:38px;text-align:right;font-size:6px;line-height:1.55;color:var(--ink-soft)}
.lh-body{position:absolute;left:40px;right:40px;top:150px;font-size:6.6px;line-height:1.75;color:var(--ink)}
.lh-body p{margin-bottom:11px;text-align:justify}
.lh-greeting{font-size:7.5px}
.lh-signature{font-family:"Pinyon Script",cursive;font-size:26px;color:#333;margin-top:20px}
.lh-footer{position:absolute;left:0;right:0;bottom:0}
.lh-band-green{height:6px;background:var(--green)}
.lh-band-gold{height:14px;background:var(--gold);display:flex;align-items:center;justify-content:center;font-size:6px;color:#fff}
</style>
</head>
<body>
<main class="canvas">

  <!-- business cards -->
  <section class="card card--dark card--logo" style="left:120px;top:36px">
    <div class="brand"><span class="brand-dot"></span>Bright Cusp Dental</div>
    <div class="card-stripe"></div>
  </section>
  <section class="card card--light card--contact" style="left:282px;top:36px">
    <div class="brand"><span class="brand-dot"></span>Bright Cusp Dental</div>
    <div class="card-name">RON TALIVERO DDS</div>
    <div class="card-role">General &amp; Cosmetic Dentistry</div>
    <div class="card-line">47-30 91 Street, Elmhurst, NY 11208</div>
    <div class="card-line">brightcuspdental@mailbox-example.com</div>
    <div class="card-stripe"></div>
  </section>
  <section class="card card--dark card--contact" style="left:444px;top:36px">
    <div class="card-name">Ron Talivero</div>
    <div class="card-role">General &amp; Cosmetic Dentistry</div>
    <div class="card-line">Tel: 718 555 0142</div>
    <div class="card-line">47-30 91 Street</div>
    <div class="card-line">Elmhurst, NY 11208</div>
    <div class="card-line">brightcuspdental@mailbox-example.com</div>
  </section>
  <section class="card card--light card--logo" style="left:120px;top:134px">
    <div class="brand"><span class="brand-dot"></span>Bright Cusp Dental</div>
    <div class="card-web">www.brightcuspdental-example.com</div>
    <div class="card-stripe"></div>
  </section>
  <section class="card card--light card--logo" style="left:282px;top:134px">
    <div class="brand"><span class="brand-dot"></span>Bright Cusp Dental</div>
    <div class="card-web">www.brightcuspdental-example.com</div>
    <div class="card-stripe"></div>
  </section>
  <section class="card card--dark card--contact" style="left:444px;top:134px">
    <div class="card-name">Ron Talivero</div>
    <div class="card-role">General &amp; Cosmetic Dentistry</div>
    <div class="card-line">Tel: 718 555 0142</div>
    <div class="card-line">47-30 91 Street</div>
    <div class="card-line">Elmhurst, NY 11208</div>
    <div class="card-line">www.brightcuspdental-example.com</div>
  </section>

  <!-- envelopes -->
  <section class="envelopes">
    <svg width="480" height="450" viewBox="0 0 480 450">
      <polygon points="0,20 480,20 480,150 0,150" fill="var(--gold)"/>
      <polygon points="0,20 80,0 400,0 480,20" fill="var(--gold-light)"/>
      <polygon points="0,90 480,90 480,220 0,220" fill="var(--green)"/>
      <polygon points="0,90 80,68 400,68 480,90" fill="var(--green-light)"/>
      <polygon points="0,170 480,170 480,450 0,450" fill="var(--paper)"/>
      <polygon points="0,170 80,150 400,150 480,170" fill="#f1f1f1"/>
      <rect x="0" y="430" width="480" height="6" fill="var(--green)"/>
      <rect x="0" y="436" width="480" height="14" fill="var(--gold)"/>
    </svg>
    <div class="env-tab" style="top:40px">Bright Cusp Dental</div>
    <div class="env-tab" style="top:110px">Bright Cusp Dental</div>
    <div class="env-tab" style="top:180px;color:var(--green)">Bright Cusp Dental</div>
    <div class="env-brand"><div class="brand"><span class="brand-dot"></span>Bright Cusp Dental</div></div>
    <div class="env-address">
      <div class="card-name">RON TALIVERO DDS</div>
      47-30 91 Street<br>Elmhurst, NY 11208
    </div>
  </section>

  <!-- letterhead -->
  <article class="letterhead">
    <div class="lh-brand"><div class="brand"><span class="brand-dot"></span>Bright Cusp Dental</div></div>
    <div class="lh-address">
      47-30 91 Street<br>Elmhurst, NY 11208<br>Tel: 718 555 0142<br>brightcuspdental@mailbox-example.com
    </div>
    <div class="lh-body">
      <p class="lh-greeting">Dear Name,</p>
      <p>Thank you for choosing our practice for your family's dental care. We are pleased to welcome you and look forward to meeting you at your first visit. Our team offers general and cosmetic treatment in a calm, friendly setting, and we take time to explain every step of your care plan.</p>
      <p>Please arrive ten minutes early and bring your insurance card, a photo ID and a list of any medicines you take. If you need to change your appointment, call our front desk at least one day ahead so we can offer the time to another patient.</p>
      <p>We look forward to helping you keep a healthy, bright smile for years to come.</p>
      <div class="lh-signature">Signature</div>
    </div>
    <footer class="lh-footer">
      <div class="lh-band-green"></div>
      <div class="lh-band-gold">www.brightcuspdental-example.com</div>
    </footer>
  </article>

</main>
</body>
</html>
```